1923 Basins & Spouts Business Card

I'm wanting to get a business card designed. Our business is 1923 Basins & Spouts
Details for the card:

1923 Basins & Spouts
Name: Gareth Vostle
Email: gareth@1923basinsandspouts.com.au
Website: www.1923basinsandspouts.com.au
Mobile: 0439 602 158
Phone: 02 5550 1843

Font of Basins & Spouts is called Snell Roundhand. Not sue what font logo text is.

I'm thinking two sided but it doesn't have to be.

```html
<!DOCTYPE html>
<html lang="en">
<head>
<meta charset="utf-8">
<title>1923 Basins &amp; Spouts – Business Card</title>
<link rel="stylesheet" href="https://fonts.googleapis.com/css2?family=Open+Sans:wght@400;600&family=Roboto:wght@700&display=swap">
<style>
  :root {
    --bg: #e9e9e9;
    --card-dark: #1f1c1d;
    --card-light: #ffffff;
    --ink-dark: #1e1e1e;
    --ink-mid: #3a3a3a;
    --ink-light: #f4f4f4;
    --ink-muted: #bdbdbd;
    --rule: #cfcfcf;
  }
  * { margin: 0; padding: 0; box-sizing: border-box; }
  html, body {
    width: 1200px; height: 1200px; overflow: hidden;
    background: var(--bg);
    font-family: "Open Sans", Arial, sans-serif;
  }
  .sheet {
    width: 1200px; height: 1200px;
    display: flex; flex-direction: column; align-items: center; justify-content: center;
    gap: 60px;
  }
  .card {
    width: 840px; height: 480px;
    position: relative;
    box-shadow: 0 10px 30px rgba(0,0,0,0.18);
  }
  /* Back side */
  .card--back {
    background: var(--card-dark);
    border-radius: 90px 14px 90px 14px;
    display: flex; flex-direction: column; align-items: center; justify-content: center;
    color: var(--ink-light);
  }
  .brand {
    display: flex; align-items: center; gap: 22px;
  }
  .brand__dot {
    width: 26px; height: 26px; border-radius: 50%;
    background: currentColor;
    flex: none;
  }
  .brand__name {
    font-family: "Open Sans", Arial, sans-serif;
    font-weight: 400;
    font-size: 50px;
    letter-spacing: 1px;
    white-space: nowrap;
  }
  .tagline {
    margin-top: 16px;
    font-size: 19px;
    color: var(--ink-muted);
    letter-spacing: 0.5px;
  }
  /* Front side */
  .card--front {
    background: var(--card-light);
    border-radius: 14px 90px 14px 90px;
    display: flex; align-items: center;
    color: var(--ink-dark);
  }
  .front__brand {
    width: 320px; height: 100%;
    display: flex; flex-direction: column; align-items: center; justify-content: center;
    gap: 16px;
  }
  .front__brand .brand__dot { width: 22px; height: 22px; }
  .front__brand .brand__name {
    font-size: 36px; text-align: center; line-height: 1.25; color: var(--ink-dark);
    white-space: normal;
  }
  .divider {
    width: 1px; height: 360px; flex: none;
    background: linear-gradient(to bottom, transparent, var(--rule) 15%, var(--rule) 85%, transparent);
  }
  .front__details { padding-left: 40px; padding-right: 30px; }
  .person {
    font-family: "Roboto", Arial, sans-serif;
    font-weight: 700;
    font-size: 32px;
    letter-spacing: 0.5px;
    text-transform: uppercase;
    margin-bottom: 28px;
  }
  .contacts { list-style: none; }
  .contacts li {
    display: flex; align-items: center; gap: 12px;
    font-size: 21px; line-height: 32px; color: var(--ink-mid);
    white-space: nowrap;
  }
  .contacts svg { width: 17px; height: 17px; flex: none; fill: var(--ink-dark); }
</style>
</head>
<body>
  <main class="sheet">
    <section class="card card--back" aria-label="Card back">
      <div class="brand">
        <span class="brand__dot"></span>
        <span class="brand__name">1923 Basins &amp; Spouts</span>
      </div>
      <p class="tagline">Heritage fittings crafted for the modern home</p>
    </section>

    <section class="card card--front" aria-label="Card front">
      <div class="front__brand">
        <span class="brand__dot"></span>
        <span class="brand__name">1923 Basins<br>&amp; Spouts</span>
      </div>
      <div class="divider"></div>
      <div class="front__details">
        <h1 class="person">Gareth Vostle</h1>
        <ul class="contacts">
          <li>
            <svg viewBox="0 0 20 20" aria-hidden="true"><path d="M2 7c0-2 3-4 8-4s8 2 8 4v1h-4V6H6v2H2zM4 9h12l1 8H3zM10 11a2 2 0 1 0 0 4a2 2 0 0 0 0-4z"/></svg>
            0439 602 158
          </li>
          <li>
            <svg viewBox="0 0 20 20" aria-hidden="true"><path d="M4 2h12v16H4zM6 4v10h8V4zM9 15h2v2H9z"/></svg>
            02 5550 1843
          </li>
          <li>
            <svg viewBox="0 0 20 20" aria-hidden="true"><path d="M2 4h16v12H2zM4 6l6 5l6-5v-0.5H4z"/></svg>
            gareth@1923basinsandspouts.com.au
          </li>
          <li>
            <svg viewBox="0 0 20 20" aria-hidden="true"><circle cx="10" cy="10" r="8"/></svg>
            www.1923basinsandspouts.com.au
          </li>
        </ul>
      </div>
    </section>
  </main>
</body>
</html>
```